Premium CBD/Hemp company needs packaging and label design

Verdant Oakfield, a premium CBD/Hemp company based in Scottsdale, Arizona is in need of a packaging and label design. We are launching with our flagship product which will be a 30 count capsule and will come in three functions: Pain Relief, Anxiety Support, and Sleep Support. For the purpose of this contest, please design packaging and label for our Anxiety Support product. Our products are physician formulated and all natural. Our main ingredient is CBD/Hemp and is complemented by specific herbs that synergistically work together to give the customer the most effective and desired result. We would like our branding to have a pharmaceutical look and feel with a focus on trust and transparency. We have uploaded our company logo that is to be used on both the packaging and label. We have also uploaded an executed branding questionnaire that will guide you to exactly what we are seeking to achieve as to the look and feel of our brand. Please feel free to contact us with any questions that you may have. The winner of this contest will have the opportunity to work with us on future projects as we will need packaging and label design for our entire Verdant Oakfield product line.

Target Market(s)

See attached branding questionnaire

Industry/Entity Type

Health And Wellness

Font styles to use
Sans Serif

Colors

Designer to choose colors to be used in the design.

Requirements
Must have
• See attached branding questionnaire; Please superimpose labels onto a cobalt blue capsule bottle (see attached)
• >>UPON REVIEW of the FIRST 8 designs, we really like the silver, mildly metallic label background in DESIGN # 21300528, we do not want metalic lettering as that would not look very "Pharmaceutical"
• >>We are in search of a look that is a bit more "Pharmaceutical" than a look that would be more commonly found in a Supplement Store
Nice to have
• "See attached branding questionnaire
Should not have
• See attached branding questionnaire; NO marijuana or cannabis plant on the packaging or label

```html
<!DOCTYPE html>
<html lang="en">
<head>
<meta charset="utf-8">
<title>Verdant Oakfield – Premium CBD Oil Labels</title>
<link href="https://fonts.googleapis.com/css2?family=Source+Sans+3:wght@400;600;700&display=swap" rel="stylesheet">
<style>
  :root {
    --page: #ffffff;
    --label-white: #ffffff;
    --navy: #2b3990;
    --brand-ink: #2b3990;
    --brand-dot: #3d8a4a;
    --premium-green: #2f5e34;
    --premium-grey: #9a9a9a;
    --green-edge: #2a6a3a;
    --green-mid: #4f8e5c;
    --orange-edge: #e8383a;
    --orange-mid: #f5923a;
    --orange-ink: #f3873a;
    --brown-edge: #a4604a;
    --brown-mid: #c47c56;
    --brown-ink: #a65b45;
    --silver-dark: #7d7d7d;
    --silver-light: #ededed;
    --gold-edge: #c9a25f;
    --gold-light: #e6cc92;
    --tab-white: #fbf8fb;
    --panel-text: #ffffff;
    --small-ink: #222222;
  }
  * { box-sizing: border-box; margin: 0; padding: 0; }
  html, body { width: 1200px; height: 622px; overflow: hidden; background: var(--page); }
  body { font-family: "Source Sans 3", sans-serif; }

  .label-row {
    position: relative;
    width: 1200px; height: 622px;
    display: flex; justify-content: center; align-items: center; gap: 50px;
  }
  .label {
    position: relative;
    width: 340px; height: 362px;
    background: var(--label-white);
    box-shadow: 0 0 0 1px #e4e4e4;
    overflow: hidden;
  }
  .label__head { height: 154px; text-align: center; padding-top: 20px; }
  .brand {
    display: inline-flex; align-items: center; gap: 6px;
    font-weight: 600; font-size: 12px; letter-spacing: 0.5px;
    color: var(--brand-ink); text-transform: uppercase;
  }
  .brand__dot { width: 14px; height: 14px; border-radius: 50%; background: var(--brand-dot); }
  .label__premium {
    margin-top: 24px;
    font-size: 21px; font-weight: 400; letter-spacing: 4px;
    color: var(--premium-green);
  }
  .label__name {
    font-size: 50px; font-weight: 700; line-height: 1; letter-spacing: 1px;
    color: var(--navy); margin-top: 2px;
  }
  .label__band { height: 18px; background: linear-gradient(90deg, var(--silver-dark), var(--silver-light) 22%, #9a9a9a 50%, var(--silver-light) 78%, var(--silver-dark)); }
  .label__panel {
    position: absolute; left: 0; right: 0; top: 172px; height: 170px;
    background: linear-gradient(90deg, var(--green-edge), var(--green-mid) 55%, var(--green-edge));
  }
  .benefits {
    list-style: none; position: absolute; left: 90px; top: 30px;
    color: var(--panel-text); font-size: 26px; line-height: 35px; font-weight: 400;
  }
  .capsule-tab {
    position: absolute; left: 0; bottom: 20px; width: 100px; height: 50px;
    background: var(--tab-white);
    clip-path: polygon(0 0, 68% 0, 100% 100%, 0 100%);
    display: flex; align-items: center; gap: 5px; padding-left: 8px;
  }
  .capsule-tab__text { font-size: 10px; font-weight: 700; line-height: 11px; color: var(--small-ink); }
  .capsule-tab svg { width: 11px; height: 20px; }
  .label__volume {
    position: absolute; right: 8px; bottom: 3px;
    font-size: 11px; color: var(--small-ink);
  }

  .label--orange .label__name { color: var(--orange-ink); }
  .label--orange .label__panel { background: linear-gradient(90deg, var(--orange-edge), var(--orange-mid) 55%, var(--orange-edge)); }
  .label--orange .capsule-tab__text { color: #e8383a; }
  .label--orange .capsule-tab svg rect { stroke: #e8383a; }

  .label--brown .label__premium { color: var(--premium-grey); }
  .label--brown .label__name { color: var(--brown-ink); }
  .label--brown .label__band { background: linear-gradient(90deg, var(--gold-edge), var(--gold-light) 50%, var(--gold-edge)); }
  .label--brown .label__panel { background: linear-gradient(90deg, var(--brown-edge), var(--brown-mid) 55%, var(--brown-edge)); }
  .label--brown .capsule-tab__text { color: var(--brown-ink); }
  .label--brown .capsule-tab svg rect { stroke: var(--brown-ink); }
</style>
</head>
<body>
<main class="label-row">
  <section class="label label--green">
    <header class="label__head">
      <div class="brand"><span class="brand__dot"></span>Verdant Oakfield</div>
      <p class="label__premium">PREMIUM</p>
      <h1 class="label__name">CBD OIL</h1>
    </header>
    <div class="label__band"></div>
    <div class="label__panel">
      <ul class="benefits"><li>- Pain Relief</li><li>- Anxiety Support</li><li>- Sleep Support</li></ul>
    </div>
    <div class="capsule-tab">
      <svg viewBox="0 0 11 20"><rect x="1" y="1" width="9" height="18" rx="4.5" fill="none" stroke="#222" stroke-width="1.3"/><line x1="1" y1="10" x2="10" y2="10" stroke="#222" stroke-width="1.3"/></svg>
      <span class="capsule-tab__text">30<br>CAPSULES</span>
    </div>
    <span class="label__volume">1oz / 30ml</span>
  </section>

  <section class="label label--orange">
    <header class="label__head">
      <div class="brand"><span class="brand__dot"></span>Verdant Oakfield</div>
      <p class="label__premium">PREMIUM</p>
      <h1 class="label__name">CBD OIL</h1>
    </header>
    <div class="label__band"></div>
    <div class="label__panel">
      <ul class="benefits"><li>- Pain Relief</li><li>- Anxiety Support</li><li>- Sleep Support</li></ul>
    </div>
    <div class="capsule-tab">
      <svg viewBox="0 0 11 20"><rect x="1" y="1" width="9" height="18" rx="4.5" fill="none" stroke="#222" stroke-width="1.3"/><line x1="1" y1="10" x2="10" y2="10" stroke="#e8383a" stroke-width="1.3"/></svg>
      <span class="capsule-tab__text">30<br>CAPSULES</span>
    </div>
    <span class="label__volume">1oz / 30ml</span>
  </section>

  <section class="label label--brown">
    <header class="label__head">
      <div class="brand"><span class="brand__dot"></span>Verdant Oakfield</div>
      <p class="label__premium">PREMIUM</p>
      <h1 class="label__name">CBD OIL</h1>
    </header>
    <div class="label__band"></div>
    <div class="label__panel">
      <ul class="benefits"><li>- Pain Relief</li><li>- Anxiety Support</li><li>- Sleep Support</li></ul>
    </div>
    <div class="capsule-tab">
      <svg viewBox="0 0 11 20"><rect x="1" y="1" width="9" height="18" rx="4.5" fill="none" stroke="#222" stroke-width="1.3"/><line x1="1" y1="10" x2="10" y2="10" stroke="#a65b45" stroke-width="1.3"/></svg>
      <span class="capsule-tab__text">30<br>CAPSULES</span>
    </div>
    <span class="label__volume">1oz / 30ml</span>
  </section>
</main>
</body>
</html>
```